Business Card Design

Looking for a clean professional Business card design with our logo. Needs to be able to customize name, address and contact info so we can use it multiple times with different people, please.

```html
<!DOCTYPE html>
<html lang="en">
<head>
<meta charset="utf-8">
<title>Brightpath Careers – Business Card</title>
<link rel="stylesheet" href="https://fonts.googleapis.com/css2?family=Source+Sans+3:wght@400;600;700&display=swap">
<style>
  :root {
    --stage: #7d7e80;
    --paper: #ececec;
    --ink: #1b1b1b;
    --brand-red: #c4202f;
    --name-red: #d42a3e;
    --muted: #6d6d6d;
    --white: #ffffff;
  }
  * { margin: 0; padding: 0; box-sizing: border-box; }
  html, body { width: 1001px; height: 1200px; overflow: hidden; }
  body {
    position: relative;
    background: var(--stage);
    font-family: "Source Sans 3", Arial, sans-serif;
    color: var(--ink);
  }
  .spec-bar {
    position: absolute; left: 275px; top: 51px; width: 461px; height: 64px;
    border-top: 4px solid var(--white); border-bottom: 4px solid var(--white);
    display: flex; align-items: center; justify-content: center;
    color: var(--white); font-size: 29px; letter-spacing: 0.5px;
  }
  .card {
    position: absolute; left: 192px; width: 642px; height: 403px;
    background: var(--paper); border-radius: 22px;
    box-shadow: 3px 6px 14px rgba(0,0,0,0.35);
  }
  .card--front { top: 150px; }
  .card--back { top: 638px; }

  .brand-square {
    position: absolute; left: 278px; top: 115px; width: 99px; height: 97px;
    background: var(--brand-red);
  }
  .divider-ornament {
    position: absolute; left: 223px; top: 236px; width: 198px; height: 6px;
    border-radius: 3px;
    background: linear-gradient(90deg, transparent, var(--ink) 12%, var(--ink) 88%, transparent);
  }
  .company-name {
    position: absolute; left: 0; width: 100%; top: 260px;
    text-align: center; font-size: 30px; font-weight: 400; letter-spacing: 0.5px;
  }
  .tagline {
    position: absolute; left: 0; width: 100%; top: 303px;
    text-align: center; font-size: 15px; font-weight: 600; letter-spacing: 3px;
  }
  .website {
    position: absolute; left: 0; width: 100%; top: 366px;
    text-align: center; font-size: 17px; font-weight: 600; letter-spacing: 3px;
    color: var(--muted);
  }

  .person { position: absolute; left: 62px; top: 158px; width: 224px; text-align: center; }
  .person__name { font-size: 32px; font-weight: 700; color: var(--name-red); letter-spacing: 0.5px; line-height: 1; }
  .person__role { font-size: 14px; font-weight: 600; margin-top: 10px; letter-spacing: 0.3px; }

  .vertical-ornament {
    position: absolute; left: 316px; top: 96px; width: 6px; height: 198px;
    border-radius: 3px;
    background: linear-gradient(180deg, transparent, var(--ink) 10%, var(--ink) 90%, transparent);
  }
  .contacts { position: absolute; left: 346px; top: 104px; list-style: none; }
  .contacts li {
    display: flex; align-items: center; height: 46px; font-size: 16px;
  }
  .contacts svg { width: 30px; height: 26px; margin-right: 14px; flex: none; fill: var(--ink); }
</style>
</head>
<body>
  <header class="spec-bar">3.2 x 2”| FULLY EDITABLE | 300 DPI</header>

  <section class="card card--front">
    <div class="brand-square"></div>
    <div class="divider-ornament" role="img" aria-label="Decorative flourish divider"></div>
    <h1 class="company-name">BRIGHTPATH CAREERS</h1>
    <p class="tagline">EMPOWER YOUR FUTURE</p>
    <p class="website">WWW.YOURWEBSITE.COM</p>
  </section>

  <section class="card card--back">
    <div class="person">
      <h2 class="person__name">MIRA DEVAN</h2>
      <p class="person__role">DESIGN ENGINEER</p>
    </div>
    <div class="vertical-ornament" role="img" aria-label="Decorative vertical flourish divider"></div>
    <ul class="contacts">
      <li>
        <svg viewBox="0 0 24 24" aria-hidden="true"><path d="M6.6 10.8a15 15 0 0 0 6.6 6.6l2.2-2.2c.3-.3.7-.4 1-.2 1.1.4 2.3.6 3.6.6.6 0 1 .4 1 1V20c0 .6-.4 1-1 1A17 17 0 0 1 3 4c0-.6.4-1 1-1h3.5c.6 0 1 .4 1 1 0 1.3.2 2.5.6 3.6.1.3 0 .7-.2 1z"/></svg>
        +91 9000012345.
      </li>
      <li>
        <svg viewBox="0 0 30 22" aria-hidden="true"><rect x="0" y="1" width="30" height="20" rx="1"/><path d="M1.5 2.5 15 13 28.5 2.5" fill="none" stroke="#ececec" stroke-width="1.6"/></svg>
        hello@brightpath.example
      </li>
      <li>
        <svg viewBox="0 0 24 28" aria-hidden="true"><rect x="5" y="1" width="14" height="26" rx="7"/><rect x="11" y="5" width="2" height="6" rx="1" fill="#ececec"/></svg>
        www.yourwebsite.com
      </li>
      <li>
        <svg viewBox="0 0 24 28" aria-hidden="true"><path d="M12 1a8 8 0 0 0-8 8c0 6 8 18 8 18s8-12 8-18a8 8 0 0 0-8-8z"/><circle cx="12" cy="9" r="3" fill="#ececec"/></svg>
        Springvale,Lakeland
      </li>
    </ul>
  </section>
</body>
</html>
```